KRL Banner Logo with Rocky Mountain of CO as the background

I need a banner/logo for my KRL year. So have a banner design that is like an intentional path or inspiring.

• KRL Silver Ridge CO mountain as background and they may add similar images that I sent you
• Wording: Intentional Path
Learning year 2025-2026
• Add the KRL logo (the white and blue image – you will see these online)

UPDATE: Attached are example images on how we envision the banner. Please do not use the attached example sample images. Kindly look for similar looking images that are FREE TO USE Commercially.

CEO, top executives

0054AA
0677BA
7BADD7
CADEEF
E8F1F8

• • KRL Silver Ridge CO mountain as background and they may add similar images that I sent you • Wording: Intentional Path Learning year 2025-2026 • Add the KRL logo (the white and blue image – you will see these online)
• It has nice to have the inspirational images attached but you can have your own design. This is only for sample.

```html
<!DOCTYPE html>
<html lang="en">
<head>
<meta charset="utf-8">
<title>Intentional Path Banner</title>
<link href="https://fonts.googleapis.com/css2?family=Crimson+Pro:wght@400&family=Montserrat:wght@600&family=Parisienne&display=swap" rel="stylesheet">
<style>
  :root {
    --page: #ffffff;
    --brand-blue: #0054aa;
    --brand-blue-deep: #0a4a9c;
    --white: #ffffff;
    --rock-dark: #5a2e22;
    --rock-mid: #9a5238;
    --rock-light: #c98a6a;
    --sky-haze: #b9a3a8;
  }
  * { margin: 0; padding: 0; box-sizing: border-box; }
  html, body {
    width: 1200px; height: 720px; overflow: hidden;
    background: var(--page);
  }
  .banner {
    position: absolute;
    left: 120px;
    width: 960px;
    height: 175px;
    overflow: hidden;
  }
  .banner--split { top: 124px; box-shadow: 0 2px 5px rgba(0,0,0,0.25); }
  .banner--blend { top: 397px; }

  .canyon-photo {
    position: absolute; inset: 0;
    background:
      radial-gradient(ellipse at 28% 40%, var(--sky-haze) 0%, transparent 35%),
      linear-gradient(100deg, var(--rock-dark) 0%, var(--rock-mid) 25%, var(--rock-light) 40%, var(--rock-mid) 55%, var(--rock-dark) 75%, var(--rock-mid) 100%);
  }
  .split-panel { position: absolute; inset: 0; }

  .blend-overlay {
    position: absolute; inset: 0;
    background: linear-gradient(90deg, transparent 0%, transparent 42%, rgba(10,74,156,0.75) 58%, var(--brand-blue-deep) 75%, var(--brand-blue) 100%);
  }

  .brand-name {
    position: absolute;
    left: 54px; top: 90px;
    font-family: "Crimson Pro", serif;
    font-weight: 400;
    font-size: 62px;
    line-height: 1;
    color: var(--white);
    letter-spacing: 1px;
  }

  .headline {
    position: absolute;
    right: 42px; top: 22px;
    text-align: right;
    color: var(--white);
  }
  .headline__year {
    font-family: "Crimson Pro", serif;
    font-size: 23px;
    line-height: 1;
    letter-spacing: 0.5px;
  }
  .headline__title {
    font-family: "Parisienne", cursive;
    font-size: 68px;
    line-height: 1;
    margin-top: 4px;
    margin-right: -4px;
  }
  .headline__chapter {
    font-family: "Montserrat", sans-serif;
    font-weight: 600;
    font-size: 14px;
    line-height: 1;
    margin-top: 2px;
  }
</style>
</head>
<body>

  <section class="banner banner--split">
    <div class="canyon-photo" role="img" aria-label="Hiker with a backpack overlooking a red rock canyon with a winding river"></div>
    <svg class="split-panel" width="960" height="175" viewBox="0 0 960 175" aria-hidden="true">
      <polygon points="498,0 960,0 960,175 342,175" fill="var(--brand-blue)"/>
    </svg>
    <div class="brand-name">KRL</div>
    <div class="headline">
      <p class="headline__year">2025-2026 Learning Year</p>
      <p class="headline__title">Intentional Path</p>
      <p class="headline__chapter">KRL Gold Silver Ridge Chapter</p>
    </div>
  </section>

  <section class="banner banner--blend">
    <div class="canyon-photo" role="img" aria-label="Hiker with a backpack overlooking a red rock canyon with a winding river, fading into blue"></div>
    <div class="blend-overlay"></div>
    <div class="brand-name">KRL</div>
    <div class="headline">
      <p class="headline__year">2025-2026 Learning Year</p>
      <p class="headline__title">Intentional Path</p>
      <p class="headline__chapter">KRL Gold Silver Ridge Chapter</p>
    </div>
  </section>

</body>
</html>
```